NEW YORK Plumbing/utility company 10 year anniversary business card

Looking For simple back and front business card would like to include a few things in description
We offer 24/7 emergency service
residential
commercial
industrial
municipal
services offered
Plumbing
hydro excavation
hydro jetting
Well pumps
Sewer pumps
water mains
sewer mains

```html
<!DOCTYPE html>
<html lang="en">
<head>
<meta charset="utf-8">
<title>Ridgeline Water &amp; Sewer – Business Cards</title>
<link rel="stylesheet" href="https://fonts.googleapis.com/css2?family=Poppins:wght@400;600;700&display=swap">
<style>
  :root {
    --backdrop: #cbcbcb;
    --paper: #ffffff;
    --brand-blue: #0062a0;
    --brand-red: #f50000;
    --ink-light: #ffffff;
  }
  * { box-sizing: border-box; margin: 0; padding: 0; }
  html, body {
    width: 1200px; height: 1085px; overflow: hidden;
    background: var(--backdrop);
    font-family: "Poppins", sans-serif;
  }
  .business-card {
    position: absolute; left: 301px;
    width: 579px; height: 343px;
    background: var(--paper);
    box-shadow: 2px 2px 2px rgba(0,0,0,.55);
    overflow: hidden;
  }
  .card-front { top: 163px; }
  .card-back { top: 542px; }

  .info-panel {
    position: absolute; left: 297px; top: 0;
    width: 282px; height: 100%;
    background: var(--brand-blue);
    color: var(--ink-light);
  }
  .brand-block {
    position: absolute; left: 37px; top: 0;
    width: 230px; height: 263px;
    display: flex; flex-direction: column; justify-content: center;
    gap: 4px;
  }
  .brand-mark {
    width: 34px; height: 34px; border-radius: 50%;
    background: var(--brand-blue); margin-bottom: 8px;
  }
  .brand-name {
    color: var(--brand-blue); font-weight: 700;
    font-size: 32px; line-height: 1.05; letter-spacing: .5px;
  }
  .brand-sub {
    color: var(--brand-blue); font-weight: 700;
    font-size: 17px; letter-spacing: 2.5px; line-height: 1.2;
  }

  .emergency-title {
    position: absolute; left: 40px; top: 56px;
    font-weight: 700; font-size: 18.5px; line-height: 1.3;
  }
  .sector-list { position: absolute; left: 0; top: 125px; list-style: none; }
  .sector-list li {
    display: flex; align-items: center;
    height: 25.5px; font-size: 17.5px;
  }
  .sector-list .pipe-line {
    display: inline-block; width: 30px; height: 3px;
    background: var(--ink-light); margin-right: 14px;
    position: relative;
  }
  .sector-list .pipe-line::after {
    content: ""; position: absolute; right: -4px; top: -3px;
    width: 9px; height: 9px; border-radius: 50%;
    background: var(--ink-light);
  }

  .services-title {
    position: absolute; left: 42px; top: 54px;
    font-weight: 600; font-size: 21px;
  }
  .service-list { position: absolute; left: 46px; top: 89px; list-style: none; }
  .service-list li {
    display: flex; align-items: center;
    height: 23.3px; font-size: 17px;
  }
  .service-list svg { width: 9px; height: 12px; margin-right: 13px; fill: var(--ink-light); }

  .contact-band {
    position: absolute; left: 0; top: 263px;
    width: 100%; height: 57px;
    background: var(--brand-red); color: var(--ink-light);
    display: flex; align-items: center; justify-content: center;
    gap: 12px; font-size: 17px; padding-right: 8px;
  }
  .contact-item { display: flex; align-items: center; gap: 5px; white-space: nowrap; }
  .contact-item svg { width: 14px; height: 14px; fill: none; stroke: var(--ink-light); stroke-width: 1.6; }
</style>
</head>
<body>

<section class="business-card card-front">
  <div class="info-panel">
    <h2 class="emergency-title">WE OFFER 24/7<br>EMERGENCY SERVICE</h2>
    <ul class="sector-list">
      <li><span class="pipe-line"></span>Residential</li>
      <li><span class="pipe-line"></span>Commercial</li>
      <li><span class="pipe-line"></span>Industrial</li>
      <li><span class="pipe-line"></span>Municipal</li>
    </ul>
  </div>
  <div class="brand-block">
    <span class="brand-mark"></span>
    <span class="brand-name">RIDGELINE</span>
    <span class="brand-sub">WATER &amp; SEWER</span>
  </div>
  <div class="contact-band">
    <span class="contact-item"><svg viewBox="0 0 16 16"><path d="M4 1.5l2.5 3-1.5 1.5c.8 2 2.5 3.7 4.5 4.5l1.5-1.5 3 2.5-1.5 2.5C7 14 2 9 1.5 3z"/></svg>845-555-0193</span>
    <span class="contact-item"><svg viewBox="0 0 16 16"><rect x="1" y="3.5" width="14" height="9"/><path d="M1 3.5l7 5 7-5"/></svg>info@ridgelinews.com</span>
    <span class="contact-item"><svg viewBox="0 0 16 16"><circle cx="8" cy="8" r="6.5"/><ellipse cx="8" cy="8" rx="3" ry="6.5"/><path d="M1.5 8h13M2.5 4.8h11M2.5 11.2h11"/></svg>www.ridgelinews.com</span>
  </div>
</section>

<section class="business-card card-back">
  <div class="info-panel">
    <h2 class="services-title">Services Offered</h2>
    <ul class="service-list">
      <li><svg viewBox="0 0 10 13"><path d="M5 0C3 4 0 6 0 8.5a5 4.5 0 0 0 10 0C10 6 7 4 5 0z"/></svg>Plumbing</li>
      <li><svg viewBox="0 0 10 13"><path d="M5 0C3 4 0 6 0 8.5a5 4.5 0 0 0 10 0C10 6 7 4 5 0z"/></svg>Hydro Excavation</li>
      <li><svg viewBox="0 0 10 13"><path d="M5 0C3 4 0 6 0 8.5a5 4.5 0 0 0 10 0C10 6 7 4 5 0z"/></svg>Hydro Jetting</li>
      <li><svg viewBox="0 0 10 13"><path d="M5 0C3 4 0 6 0 8.5a5 4.5 0 0 0 10 0C10 6 7 4 5 0z"/></svg>Well Pumps</li>
      <li><svg viewBox="0 0 10 13"><path d="M5 0C3 4 0 6 0 8.5a5 4.5 0 0 0 10 0C10 6 7 4 5 0z"/></svg>Sewer Pumps</li>
      <li><svg viewBox="0 0 10 13"><path d="M5 0C3 4 0 6 0 8.5a5 4.5 0 0 0 10 0C10 6 7 4 5 0z"/></svg>Water Mains</li>
      <li><svg viewBox="0 0 10 13"><path d="M5 0C3 4 0 6 0 8.5a5 4.5 0 0 0 10 0C10 6 7 4 5 0z"/></svg>Sewer Mains</li>
    </ul>
  </div>
  <div class="brand-block">
    <span class="brand-mark"></span>
    <span class="brand-name">RIDGELINE</span>
    <span class="brand-sub">WATER &amp; SEWER</span>
  </div>
  <div class="contact-band">
    <span class="contact-item"><svg viewBox="0 0 16 16"><path d="M4 1.5l2.5 3-1.5 1.5c.8 2 2.5 3.7 4.5 4.5l1.5-1.5 3 2.5-1.5 2.5C7 14 2 9 1.5 3z"/></svg>845-555-0193</span>
    <span class="contact-item"><svg viewBox="0 0 16 16"><rect x="1" y="3.5" width="14" height="9"/><path d="M1 3.5l7 5 7-5"/></svg>info@ridgelinews.com</span>
    <span class="contact-item"><svg viewBox="0 0 16 16"><circle cx="8" cy="8" r="6.5"/><ellipse cx="8" cy="8" rx="3" ry="6.5"/><path d="M1.5 8h13M2.5 4.8h11M2.5 11.2h11"/></svg>www.ridgelinews.com</span>
  </div>
</section>

</body>
</html>
```